Business Card, Stationary Layout, AND Powerpoint template for an IT Services Company
Silver Harbor Systems
Business Card, Stationary Layout, AND Powerpoint template for an IT Services Company - Information Technology
Creative Brief
Modern
Dean Harrow
President & CEO
40627 Birch Hollow Ln. Brookfield, MD 20349
Dean.Harrow@SilverHarborSystems.example
www.silverharborsystems.example
Perhaps a very light version of my logo graphic.

```html
<!DOCTYPE html>
<html lang="en">
<head>
<meta charset="utf-8">
<title>Silver Harbor Systems – Business Card</title>
<link href="https://fonts.googleapis.com/css2?family=Michroma&family=Open+Sans:wght@400;600;700&display=swap" rel="stylesheet">
<style>
  :root {
    --page-bg: #e6e7e9;
    --card-bg: #ffffff;
    --ink: #3b3d40;
    --ink-soft: #6b6e72;
    --accent-blue: #1b8fd4;
    --accent-orange: #f29a1f;
    --mark-tint: #dfe9f1;
    --shadow: rgba(0,0,0,0.16);
  }
  * { margin: 0; padding: 0; box-sizing: border-box; }
  html, body { width: 1200px; height: 1023px; overflow: hidden; }
  body {
    background: var(--page-bg);
    font-family: "Open Sans", Arial, sans-serif;
    color: var(--ink);
    position: relative;
  }
  .card-set {
    position: absolute;
    left: 40px;
    top: 357px;
    display: flex;
    gap: 40px;
  }
  .card {
    position: relative;
    width: 540px;
    height: 309px;
    background: var(--card-bg);
    border-radius: 10px;
    box-shadow: 0 6px 18px var(--shadow);
    overflow: hidden;
  }
  .brand {
    display: flex;
    align-items: center;
    gap: 12px;
    font-family: "Michroma", "Open Sans", sans-serif;
    color: var(--ink);
    text-transform: uppercase;
    line-height: 1;
    white-space: nowrap;
  }
  .brand-dot {
    flex: none;
    border-radius: 50%;
    background: var(--accent-blue);
  }
  .front .brand { position: absolute; left: 30px; top: 32px; font-size: 15px; z-index: 1; }
  .front .brand-dot { width: 26px; height: 26px; }
  .person { position: absolute; left: 30px; top: 108px; }
  .person-name { font-size: 15px; font-weight: 700; }
  .person-title { font-size: 12px; font-weight: 600; color: var(--ink-soft); margin-top: 2px; }
  .contact {
    position: absolute;
    left: 30px;
    top: 172px;
    font-size: 11px;
    line-height: 1.55;
    color: var(--ink);
    z-index: 1;
  }
  .contact .gap { height: 8px; }
  .contact-line { display: flex; align-items: center; gap: 6px; }
  .contact-line svg { width: 10px; height: 10px; fill: var(--accent-orange); flex: none; }
  .web { position: absolute; left: 30px; bottom: 22px; font-size: 11px; color: var(--ink-soft); }
  .front .mark-area {
    position: absolute;
    right: -70px;
    top: 44px;
    width: 220px;
    height: 220px;
    border-radius: 50%;
    background: var(--mark-tint);
  }
  .back .mark-area {
    position: absolute;
    left: -60px;
    top: 44px;
    width: 220px;
    height: 220px;
    border-radius: 50%;
    background: var(--mark-tint);
  }
  .back .brand {
    position: absolute;
    left: 200px;
    top: 138px;
    font-size: 24px;
    letter-spacing: 0.5px;
    flex-direction: column;
    align-items: flex-start;
    gap: 8px;
  }
  .back .brand .sub { font-size: 14px; letter-spacing: 3px; color: var(--ink); }
</style>
</head>
<body>
  <main class="card-set">
    <section class="card front" aria-label="Business card front">
      <div class="mark-area" role="img" aria-label="Large light brand emblem decoration"></div>
      <div class="brand"><span class="brand-dot"></span><span>Silver Harbor Systems</span></div>
      <div class="person">
        <div class="person-name">Dean Harrow</div>
        <div class="person-title">President &amp; CEO</div>
      </div>
      <div class="contact">
        <div>40627 Birch Hollow Ln.</div>
        <div>Brookfield, MD 20349</div>
        <div class="gap"></div>
        <div class="contact-line">
          <svg viewBox="0 0 10 10"><rect x="0" y="0" width="10" height="10" rx="2"/></svg>
          <span>(410) 555-0147</span>
        </div>
        <div class="contact-line">
          <svg viewBox="0 0 10 10"><rect x="0" y="0" width="10" height="10" rx="2"/></svg>
          <span>Dean.Harrow@SilverHarborSystems.example</span>
        </div>
      </div>
      <div class="web">www.silverharborsystems.example</div>
    </section>

    <section class="card back" aria-label="Business card back">
      <div class="mark-area" role="img" aria-label="Large light brand emblem decoration"></div>
      <div class="brand">
        <span>Silver Harbor</span>
        <span class="sub">Systems</span>
      </div>
    </section>
  </main>
</body>
</html>
```